Lionel Varkestone and Dennis Holtby Advertisement

We would like an ad that conveys understated elegance. We are a company that purchases estate jewelry watches and diamonds. We care to a wealthy, upscale clientele.

Target Market(s)

Wealthy upscale.

Industry/Entity Type

It Company

Requirements
Must have
• Elegant Design. Crisp Clean. Attached a doc of how the ad should be arranged.

```html
<!DOCTYPE html>
<html lang="en">
<head>
<meta charset="utf-8">
<title>Lionel Varkestone &amp; Dennis Holtby — Ready to Sell?</title>
<link rel="stylesheet" href="https://fonts.googleapis.com/css2?family=Pinyon+Script&family=Forum&family=Marcellus+SC&family=Courier+Prime&display=swap">
<style>
  :root {
    --page: #ffffff;
    --ink-deep: #0b0b0b;
    --ink-mid: #1d1f1f;
    --ink-soft: #3a3d3c;
    --silver: #e4e6e6;
    --silver-soft: #c9cccc;
    --silver-dim: #9a9d9d;
    --stone-core: #f4f6f7;
    --stone-edge: #cfd3d5;
  }
  * { margin: 0; padding: 0; box-sizing: border-box; }
  html, body {
    width: 1000px; height: 1200px; overflow: hidden;
    background: var(--page);
  }
  .ad {
    position: absolute; left: 102px; top: 18px;
    width: 796px; height: 1162px; overflow: hidden;
    background:
      radial-gradient(ellipse 520px 300px at 82% 8%, var(--ink-soft) 0%, transparent 70%),
      radial-gradient(ellipse 600px 260px at 70% 78%, #2a2c2c 0%, transparent 70%),
      linear-gradient(160deg, var(--ink-mid) 0%, var(--ink-deep) 45%, #151616 100%);
    color: var(--silver);
    text-align: center;
  }
  .ad__headline {
    position: absolute; left: 0; right: 0; top: 66px;
    font-family: "Pinyon Script", cursive;
    font-weight: 400;
    font-size: 108px; line-height: 1;
    color: var(--silver);
  }
  .ad__stone {
    position: absolute; left: 0; top: 200px;
    width: 796px; height: 440px;
    background:
      radial-gradient(ellipse 170px 165px at 51.5% 40%, var(--stone-core) 0%, var(--stone-edge) 42%, rgba(120,124,126,0.35) 72%, rgba(120,124,126,0) 100%),
      radial-gradient(ellipse 260px 34px at 36% 72%, rgba(255,255,255,0.55) 0%, rgba(255,255,255,0) 100%),
      radial-gradient(ellipse 380px 150px at 40% 50%, rgba(255,255,255,0.10) 0%, rgba(255,255,255,0) 100%);
  }
  .brand {
    position: absolute; left: 0; right: 0; top: 660px;
  }
  .brand__mark {
    width: 14px; height: 14px; margin: 0 auto 34px;
    background: var(--silver-soft);
  }
  .brand__name {
    font-family: "Marcellus SC", serif;
    font-size: 20px; letter-spacing: 0.5px;
    color: var(--silver);
  }
  .brand__tagline {
    display: flex; align-items: center; justify-content: center; gap: 8px;
    margin-top: 2px;
    font-family: "Marcellus SC", serif;
    font-size: 8px; letter-spacing: 0.6px;
    color: var(--silver-soft);
  }
  .brand__tagline::before, .brand__tagline::after {
    content: ""; width: 72px; height: 1px; background: var(--silver-dim);
  }
  .ad__promise {
    position: absolute; left: 0; right: 0; top: 852px;
    font-family: "Forum", serif;
    font-size: 54px; line-height: 1;
    color: var(--silver-soft);
    -webkit-text-stroke: 0.6px var(--silver-soft);
  }
  .ad__booking {
    position: absolute; left: 0; right: 0; top: 940px;
    font-family: "Forum", serif;
    font-size: 37px; line-height: 1;
    color: var(--silver);
    -webkit-text-stroke: 0.3px var(--silver);
  }
  .contact {
    position: absolute; left: 0; right: 0; top: 1002px;
    font-family: "Courier Prime", monospace;
    font-size: 19px; line-height: 27px; letter-spacing: 1px;
    color: var(--silver);
    list-style: none;
  }
</style>
</head>
<body>
  <main class="ad">
    <h1 class="ad__headline">Ready to Sell?</h1>
    <div class="ad__stone" role="img" aria-label="Emerald-cut diamond glowing in a beam of light"></div>

    <div class="brand">
      <div class="brand__mark"></div>
      <p class="brand__name">Lionel Varkestone &amp; Dennis Holtby</p>
      <p class="brand__tagline">YOUR BEST OPTION</p>
    </div>

    <p class="ad__promise">Utmost Discretion</p>
    <p class="ad__booking">By Appointment</p>

    <ul class="contact">
      <li class="contact__street">Via Solenne | 118-B Larkmoor Avenue</li>
      <li class="contact__city">Coral Haven, FL 33999</li>
      <li class="contact__email">support@varkholtby.com</li>
      <li class="contact__phone">555.014.2290</li>
    </ul>
  </main>
</body>
</html>
```